Seasoned logs and kindling for sale

producing firewood from beech,ash,oak and silver birch,
Kindling is produce from a variety of seasoned softwoods

Industry/Entity Type

Firewood

Contact Information for Business Card

mark Pellew 07812603948
dave Tillard 07846217035
e-mail,markp318@mailbrook.net

```html
<!DOCTYPE html>
<html lang="en">
<head>
<meta charset="utf-8">
<title>Pellew &amp; Tillard – Seasoned Logs and Kindling</title>
<link rel="stylesheet" href="https://fonts.googleapis.com/css2?family=Libre+Baskerville&display=swap">
<style>
  :root {
    --page: #ffffff;
    --card-border: #1b1b1b;
    --card-shadow: #9a9a9a;
    --deep-blue: #03476a;
    --navy: #06274f;
    --stone: #c3c4c4;
    --band: rgba(170, 200, 210, 0.5);
    --ink: #0b2b56;
    --divider-light: #e6eef2;
    --divider-dark: #0a5a85;
  }
  * { margin: 0; padding: 0; box-sizing: border-box; }
  html, body {
    width: 1200px;
    height: 675px;
    overflow: hidden;
    background: var(--page);
  }
  .canvas {
    position: relative;
    width: 1200px;
    height: 675px;
  }
  .business-card {
    position: absolute;
    left: 40px;
    top: 18px;
    width: 1120px;
    height: 639px;
    border: 1.5px solid var(--card-border);
    box-shadow: 5px 5px 0 var(--card-shadow);
    background: var(--stone);
    overflow: hidden;
    font-family: "Libre Baskerville", "Bookman Old Style", serif;
    color: var(--ink);
  }
  .card-background {
    position: absolute;
    inset: 0;
    width: 100%;
    height: 100%;
  }
  .contact-band {
    position: absolute;
    left: 0;
    top: 190px;
    width: 100%;
    height: 93px;
    background: var(--band);
    display: flex;
  }
  .contact {
    flex: 1;
    display: flex;
    flex-direction: column;
    justify-content: center;
    gap: 12px;
    font-size: 21px;
    letter-spacing: 0.5px;
    text-transform: uppercase;
  }
  .contact--left { align-items: center; padding-right: 120px; }
  .contact--right { align-items: center; padding-left: 120px; }
  .contact-name, .contact-phone { line-height: 1; }
  .band-divider {
    width: 4px;
    height: 100%;
    background: linear-gradient(to bottom, var(--divider-light), var(--divider-dark) 50%, var(--divider-light));
  }
  .email-line {
    position: absolute;
    left: 0;
    width: 100%;
    top: 548px;
    text-align: center;
    font-size: 36px;
    line-height: 1.2;
  }
</style>
</head>
<body>
<main class="canvas">
  <section class="business-card" aria-label="Pellew and Tillard firewood business card">
    <svg class="card-background" viewBox="0 0 1120 639" preserveAspectRatio="none" aria-hidden="true">
      <path d="M0 0 H1120 V402 Q560 612 0 402 Z" fill="var(--navy)"/>
      <path d="M0 0 H1120 V402 Q560 564 0 402 Z" fill="var(--deep-blue)"/>
    </svg>

    <div class="contact-band">
      <div class="contact contact--left">
        <span class="contact-name">mark Pellew</span>
        <span class="contact-phone">07812603948</span>
      </div>
      <div class="band-divider" aria-hidden="true"></div>
      <div class="contact contact--right">
        <span class="contact-name">dave Tillard</span>
        <span class="contact-phone">07846217035</span>
      </div>
    </div>

    <p class="email-line">E-mail : markp318@mailbrook.net</p>
  </section>
</main>
</body>
</html>
```